CRANDEL'S needs a label design for a Moruga Scorpion Pepper Hot Sauce (5oz bottle)

We need a label for a new company based in south Mississippi called CRANDEL'S. We have a new hot sauce made from Moruga Scorpion Peppers that's very hot yet has "layers of flavor". The sauce is a deep red color in a clear bottle. We are looking for something simple yet different and will stand out. We would like to limit the design to 3 colors.

• wide latin?

```html
<!DOCTYPE html>
<html lang="en">
<head>
<meta charset="utf-8">
<title>Crandel's Moruga Scorpion Pepper Sauce Label</title>
<link href="https://fonts.googleapis.com/css2?family=Alfa+Slab+One&family=Ultra&family=Marcellus&family=Roboto:wght@400&display=swap" rel="stylesheet">
<style>
  :root {
    --label-black: #0b0b0d;
    --pepper-red: #c4161c;
    --deep-red: #8a0c10;
    --cream-white: #f4f1ec;
    --rule-grey: #6d6d70;
  }
  html, body {
    margin: 0;
    padding: 0;
    overflow: hidden;
    background: var(--label-black);
  }
  .label {
    position: relative;
    width: 1200px;
    height: 749px;
    background: var(--label-black);
    overflow: hidden;
  }
  .brand-name {
    position: absolute;
    top: 100px;
    left: 0;
    width: 100%;
    margin: 0;
    text-align: center;
    font-family: "Marcellus", serif;
    font-weight: 400;
    font-size: 56px;
    line-height: 1;
    color: var(--cream-white);
    letter-spacing: 2px;
  }
  .product-name {
    position: absolute;
    top: 318px;
    left: 0;
    width: 100%;
    margin: 0;
    text-align: center;
    font-family: "Ultra", "Alfa Slab One", serif;
    font-weight: 400;
    font-size: 68px;
    line-height: 1;
    color: var(--pepper-red);
    letter-spacing: 6px;
  }
  .product-variety {
    position: absolute;
    top: 396px;
    left: 0;
    width: 100%;
    margin: 0;
    text-align: center;
    font-family: "Ultra", "Alfa Slab One", serif;
    font-size: 26px;
    line-height: 1;
    color: var(--pepper-red);
    letter-spacing: 1px;
  }
  .heat-level {
    position: absolute;
    top: 484px;
    left: 0;
    width: 100%;
    margin: 0;
    text-align: center;
    font-family: "Marcellus", serif;
    font-size: 44px;
    line-height: 1;
    color: var(--cream-white);
  }
  .ingredients {
    position: absolute;
    top: 566px;
    left: 60px;
    width: 208px;
  }
  .ingredients-title {
    margin: 0 0 18px;
    font-family: "Roboto", sans-serif;
    font-size: 13px;
    color: var(--cream-white);
    letter-spacing: 0.5px;
  }
  .ingredients-lines {
    display: block;
  }
  .pepper-photo {
    position: absolute;
    left: 500px;
    top: 600px;
    width: 214px;
    height: 118px;
    border-radius: 40% 45% 30% 30%;
    background: radial-gradient(ellipse at 50% 40%, #e0242a 0%, var(--pepper-red) 45%, var(--deep-red) 80%, var(--label-black) 100%);
  }
  .origin {
    position: absolute;
    right: 8px;
    top: 717px;
    margin: 0;
    font-family: "Roboto", sans-serif;
    font-size: 12.5px;
    color: var(--cream-white);
    letter-spacing: 0.3px;
  }
</style>
</head>
<body>
  <main class="label">
    <h1 class="brand-name">CRANDEL'S</h1>

    <h2 class="product-name">MORUGA</h2>
    <p class="product-variety">SCORPION PAPPER</p>

    <p class="heat-level">VERY HOT</p>

    <section class="ingredients">
      <p class="ingredients-title">INGREDIENTS :</p>
      <svg class="ingredients-lines" width="208" height="100" viewBox="0 0 208 100" aria-hidden="true">
        <g stroke="var(--rule-grey)" stroke-width="1" stroke-dasharray="1 2">
          <line x1="0" y1="0.5" x2="208" y2="0.5"/>
          <line x1="0" y1="13.5" x2="208" y2="13.5"/>
          <line x1="0" y1="26.5" x2="208" y2="26.5"/>
          <line x1="0" y1="39.5" x2="208" y2="39.5"/>
          <line x1="0" y1="52.5" x2="208" y2="52.5"/>
          <line x1="0" y1="65.5" x2="208" y2="65.5"/>
          <line x1="0" y1="78.5" x2="208" y2="78.5"/>
          <line x1="0" y1="91.5" x2="208" y2="91.5"/>
        </g>
      </svg>
    </section>

    <div class="pepper-photo" role="img" aria-label="Photograph of two glossy red Moruga Scorpion peppers"></div>

    <p class="origin">MADE IN SOUTH MISSISSIPPI</p>
  </main>
</body>
</html>
```